Business Card Design

The image I attached was a quick thought to my design. I have triplets and was invisioning something with three figures with maybe the colors blue, pink and green. I would like it to look very chic and modern yet soothing/healing. I will take any fresh ideas as well.

Side 1: Contact Details
Side 2: Appointment section (mandatory)

Thank u all for your preliminary designs. I had sent the old design over and am looking for a bold fresh NEW LOOK  for CORE MOTION. I saw some really creative ideas in the gallery. If you have any other questions please feel free to email me at rtbaxley@plumnet.example.

Thanks

Please keep in mind that it is mandatory that on the back of the card is for appointments.

Thank you.

Reason: The two mandatory elements that need to be on the card is that her title needs to read as so:

Reason: The criteria is still not being met. Her title needs to read as so: Dr. Marcia Whitfield, P.T., D.P.T. Doctor of Physical Therapy and The appointment info must go on the BACK of the card. Looking forward to some more great designs. Thanks.

Industry/Entity Type

Business

Contact Information for Business Card

Core Motion
Physical & Aquatic Therapy
Dr. Marcia Whitfield, P.T., D.P.T.
Doctor of Physical Therapy

22-37 B Birchmere Lane
Wrenfield, N.Y. 11990
(Located inside of the Pulse gym in the KMR shopping center)

Phone & Fax: (555) 812-4076
Kbrask7@quillmail.example

Requirements
Must have
• One the back I would like to do an appointment layout.

```html
<!DOCTYPE html>
<html lang="en">
<head>
<meta charset="utf-8">
<title>Core Motion Physical &amp; Aquatic Therapy – Business Card</title>
<link rel="stylesheet" href="https://fonts.googleapis.com/css2?family=Open+Sans:wght@400;600;700&family=Pinyon+Script&family=Oxygen+Mono&display=swap">
<style>
  :root {
    --page: #eceef1;
    --card: #ffffff;
    --blue: #2a95d3;
    --ink: #161616;
    --soft-ink: #3a3a3a;
    --shadow: rgba(20, 30, 45, 0.16);
  }
  * { margin: 0; padding: 0; box-sizing: border-box; }
  html, body {
    width: 1200px; height: 903px; overflow: hidden;
    background: var(--page);
    font-family: "Open Sans", Arial, sans-serif;
    color: var(--ink);
  }
  .card {
    position: absolute;
    top: 297px;
    width: 540px; height: 310px;
    background: var(--card);
    box-shadow: 0 6px 22px var(--shadow);
  }
  .card--back { left: 40px; }
  .card--front { left: 620px; }

  .brand-mark {
    position: absolute; left: 28px; top: 30px;
    width: 34px; height: 34px;
    background: var(--blue);
  }
  .brand-title {
    position: absolute; left: 74px; top: 33px;
    font-size: 20px; font-weight: 700; white-space: nowrap;
    letter-spacing: -0.2px;
  }
  .brand-title .name { color: var(--blue); }
  .brand-rule {
    position: absolute; left: 28px; right: 0; top: 72px;
    height: 2px; background: var(--blue);
  }
  .brand-tick {
    position: absolute; left: 44px; top: 72px;
    width: 2px; height: 26px; background: var(--blue);
  }

  /* back: appointment side */
  .appointment {
    position: absolute; left: 74px; right: 40px;
    display: flex; align-items: flex-end; gap: 10px;
    font-size: 13px; font-weight: 700;
  }
  .appointment--date { top: 150px; }
  .appointment--time { top: 205px; }
  .appointment .fill-line {
    flex: 1; height: 1px; background: var(--blue); margin-bottom: 4px;
  }

  /* front: contact side */
  .practitioner {
    position: absolute; right: 30px; top: 92px;
    text-align: right;
  }
  .practitioner__name { font-size: 20px; font-weight: 700; }
  .practitioner__title {
    font-family: "Pinyon Script", cursive;
    font-size: 19px; color: var(--soft-ink);
    padding-bottom: 2px;
    border-bottom: 1px solid var(--blue);
    display: inline-block; min-width: 250px;
  }
  .email {
    position: absolute; right: 30px; top: 160px; text-align: left;
  }
  .label { font-size: 10px; font-weight: 600; color: var(--soft-ink); }
  .email__address {
    font-family: "Oxygen Mono", monospace; font-size: 16px;
  }
  .phone { position: absolute; left: 30px; top: 196px; }
  .phone__number {
    font-family: "Oxygen Mono", monospace; font-size: 21px; color: var(--soft-ink);
  }
  .address { position: absolute; left: 30px; top: 250px; }
  .address__street {
    font-size: 14.5px; font-weight: 700; color: var(--blue); white-space: nowrap;
  }
  .address__note { font-size: 10.5px; font-weight: 700; white-space: nowrap; }
</style>
</head>
<body>

<section class="card card--back" aria-label="Card back: appointment">
  <div class="brand-mark"></div>
  <div class="brand-title"><span class="name">Core Motion Physical</span> &amp; Aquatic Therapy</div>
  <div class="brand-rule"></div>
  <div class="brand-tick"></div>

  <div class="appointment appointment--date">Appoinment Date:<span class="fill-line"></span></div>
  <div class="appointment appointment--time">Appoinment Time:<span class="fill-line"></span></div>
</section>

<section class="card card--front" aria-label="Card front: contact details">
  <div class="brand-mark"></div>
  <div class="brand-title"><span class="name">Core Motion Physical</span> &amp; Aquatic Therapy</div>
  <div class="brand-rule"></div>
  <div class="brand-tick"></div>

  <div class="practitioner">
    <div class="practitioner__name">Dr. Marcia Whitfield, P.T., D.P.T.</div>
    <div class="practitioner__title">Doctor of Physical Therapy</div>
  </div>

  <div class="email">
    <div class="label">e-mail:</div>
    <div class="email__address">Kbrask7@quillmail.example</div>
  </div>

  <div class="phone">
    <div class="label">Phone &amp; Fax:</div>
    <div class="phone__number">(555) 812-4076</div>
  </div>

  <div class="address">
    <div class="address__street">22-37 B Birchmere Lane Wrenfield, N.Y. 11990</div>
    <div class="address__note">(Located inside of the Pulse gym in the KMR shopping center)</div>
  </div>
</section>

</body>
</html>
```